Crispy Jerky Packaging for KO.MU

We need packaging for for our hand-crafted crispy beef jerky. We are launching a new product that is like eating a potato chip, but made of beef/pork. We would like to have a window for people to be able to see our product. It is a new type of jerky, so we need the audience to be able to see that they are getting value for what they are paying for. Where a traditional 1oz portion of jerky would have 10-11g protein, ours has 20g of protein. It is also easy on the jaw because there is no tearing off of the jerky, it eats just like a chip
Updates

Target Market(s)

Beer lovers/ health-conscious/ millenials

Industry/Entity Type

Product

Font styles to use
Other font styles liked:
• be creative

Colors
fbed22
9bcb3b
85cae6

Requirements
Must have
• Yellow packaging base
• 20g Protein per serving
• Made in Hawaii
Nice to have
• Would prefer the current font we have for the company name, KO.MU
Should not have
• cows

```html
<!DOCTYPE html>
<html lang="en">
<head>
<meta charset="utf-8">
<title>KO.MU Crispy Beef Jerky Packaging</title>
<link href="https://fonts.googleapis.com/css2?family=Bebas+Neue&family=Oswald:wght@500;700&family=Alfa+Slab+One&family=Montserrat:wght@600;700&family=Roboto+Condensed:wght@400;700&family=Lora&display=swap" rel="stylesheet">
<style>
  :root {
    --bg: #a7a8ab;
    --pouch: #ffffff;
    --blue: #3f7cc4;
    --blue-dark: #2d62a8;
    --yellow: #f5ea1f;
    --ink: #111111;
    --text-grey: #333333;
    --claim-light: #f3e6dc;
  }
  * { margin: 0; padding: 0; box-sizing: border-box; }
  html, body { width: 1200px; height: 1010px; overflow: hidden; background: var(--bg); }
  .canvas { position: relative; width: 1200px; height: 1010px; }
  .abs { position: absolute; }

  .panel {
    position: absolute; top: 192px; width: 432px; height: 656px;
    background: var(--pouch); border-radius: 18px; overflow: hidden;
  }
  .panel--front { left: 120px; }
  .panel--back { left: 622px; }

  .tagline-tab {
    position: absolute; top: 0; left: 91px; width: 251px; height: 86px;
    background: var(--blue); color: #fff;
    font-family: "Bebas Neue", sans-serif; font-size: 30px; letter-spacing: 0.5px;
    display: flex; align-items: center; justify-content: center; padding-top: 14px;
  }

  .brand {
    position: absolute; left: 0; width: 100%; text-align: center;
    font-family: "Oswald", sans-serif; font-weight: 700; color: var(--ink);
    line-height: 1; letter-spacing: 2px;
  }
  .panel--front .brand { top: 116px; font-size: 98px; }
  .panel--back .brand { top: 104px; font-size: 88px; }

  /* Blue product label */
  .label-box {
    position: absolute; background: var(--blue); color: #fff; text-align: center;
    border-radius: 12px 12px 0 0;
  }
  .label-box > div { position: absolute; left: 0; width: 100%; white-space: nowrap; }
  .label-kicker { font-family: "Montserrat", sans-serif; font-weight: 700; letter-spacing: 3px; }
  .label-title { font-family: "Bebas Neue", sans-serif; line-height: 1; }
  .label-origin { font-family: "Montserrat", sans-serif; font-weight: 700; }

  .panel--front .label-box { left: 50px; top: 266px; width: 336px; height: 118px; }
  .panel--front .label-kicker { top: 16px; font-size: 10px; }
  .panel--front .label-title { top: 30px; font-size: 64px; letter-spacing: 6px; padding-left: 6px; }
  .panel--front .label-origin { top: 93px; font-size: 11px; }

  .panel--back .label-box { left: 82px; top: 228px; width: 269px; height: 94px; }
  .panel--back .label-kicker { top: 10px; font-size: 8px; letter-spacing: 2.5px; }
  .panel--back .label-title { top: 22px; font-size: 52px; letter-spacing: 4px; padding-left: 4px; }
  .panel--back .label-origin { top: 75px; font-size: 9px; }

  /* Yellow flavour band */
  .flavour-band {
    position: absolute; background: var(--yellow); text-align: center; color: var(--ink);
    display: flex; flex-direction: column; justify-content: center;
  }
  .flavour-name { font-family: "Alfa Slab One", serif; line-height: 1.05; }
  .flavour-sub { font-family: "Roboto Condensed", sans-serif; font-weight: 700; letter-spacing: 3px; }
  .panel--front .flavour-band { left: 44px; top: 376px; width: 340px; height: 70px; }
  .panel--front .flavour-name { font-size: 36px; }
  .panel--front .flavour-sub { font-size: 12px; }
  .panel--back .flavour-band { left: 72px; top: 320px; width: 286px; height: 48px; }
  .panel--back .flavour-name { font-size: 26px; }
  .panel--back .flavour-sub { font-size: 9px; letter-spacing: 2.5px; }

  .claims {
    position: absolute; left: 0; width: 100%; text-align: center; white-space: nowrap;
    font-family: "Oswald", sans-serif; font-weight: 500; word-spacing: 3px;
  }
  .panel--front .claims { top: 452px; font-size: 14px; color: var(--claim-light); }
  .panel--back .claims { top: 372px; font-size: 12px; color: var(--ink); }

  .protein-badge {
    position: absolute; left: 180px; top: 524px; width: 72px; height: 72px; border-radius: 50%;
    background: #fff; border: 3px solid var(--blue); text-align: center; color: var(--blue-dark);
  }
  .protein-badge .amount { font-family: "Oswald", sans-serif; font-weight: 700; font-size: 24px; line-height: 1; margin-top: 8px; }
  .protein-badge .unit { font-family: "Roboto Condensed", sans-serif; font-weight: 700; font-size: 10px; letter-spacing: 1px; color: var(--ink); line-height: 1.1; }
  .protein-badge .per { font-family: "Roboto Condensed", sans-serif; font-size: 5px; color: var(--ink); }

  .net-weight {
    position: absolute; left: 0; width: 100%; text-align: center; top: 634px;
    font-family: "Roboto Condensed", sans-serif; font-weight: 700; font-size: 12px; letter-spacing: 3px;
  }

  .story {
    position: absolute; left: 96px; width: 240px; top: 396px; text-align: center;
    font-family: "Lora", serif; font-size: 8.5px; line-height: 1.35; color: var(--text-grey);
  }
  .fine {
    position: absolute; font-family: "Roboto Condensed", sans-serif; font-size: 6.5px;
    line-height: 1.3; color: var(--text-grey);
  }
  .maker {
    position: absolute; left: 89px; top: 528px; width: 140px; text-align: center;
  }
  .maker .fine { position: static; }
  .brand-small {
    font-family: "Oswald", sans-serif; font-weight: 700; font-size: 24px; line-height: 1.1;
    color: var(--blue-dark); letter-spacing: 1px;
  }

  .nutrition {
    position: absolute; left: 250px; top: 482px; width: 86px; border: 1.5px solid var(--ink);
    padding: 2px; font-family: "Roboto Condensed", sans-serif; font-size: 4.5px; color: var(--ink);
  }
  .nutrition h3 { font-size: 11px; font-weight: 700; border-bottom: 1px solid var(--ink); }
  .nutrition table { width: 100%; border-collapse: collapse; }
  .nutrition td { border-bottom: 0.5px solid var(--ink); padding: 0.5px 0; }
  .nutrition .head td { border-bottom: 3px solid var(--ink); }
</style>
</head>
<body>
<main class="canvas">

  <section class="panel panel--front">
    <div class="tagline-tab">It eats just like a chip</div>
    <div class="brand">KO.MU</div>

    <svg class="abs" style="left:0;top:0;" width="432" height="656" viewBox="0 0 432 656">
      <defs>
        <linearGradient id="jerkyTone" x1="0" y1="0" x2="1" y2="1">
          <stop offset="0" stop-color="#8a3c26"/>
          <stop offset="0.5" stop-color="#5a2316"/>
          <stop offset="1" stop-color="#7a3422"/>
        </linearGradient>
      </defs>
      <path d="M60 380 L376 380 L376 504 L218 600 L60 504 Z" fill="url(#jerkyTone)" role="img" aria-label="Product window showing pieces of crispy beef jerky"/>
      <path d="M60 380 L60 504 L218 600 L376 504 L376 380" fill="none" stroke="var(--blue)" stroke-width="2"/>
    </svg>

    <div class="label-box">
      <div class="label-kicker">• QUALITY HANDMADE •</div>
      <div class="label-title">BEEF JERKY</div>
      <div class="label-origin">MADE IN HAWAII</div>
    </div>
    <div class="flavour-band">
      <div class="flavour-name">ORIGINAL</div>
      <div class="flavour-sub">(CHIPOTLE + TERIYAKI)</div>
    </div>
    <div class="claims">LOW FAT&nbsp; HIGH PROTEIN&nbsp; GLUTEN FREE</div>

    <div class="protein-badge">
      <div class="amount">20G</div>
      <div class="unit">PROTEIN</div>
      <div class="per">PER SERVING</div>
    </div>
    <div class="net-weight">NET WT. 1.25 OZ (35G)</div>
  </section>

  <section class="panel panel--back">
    <div class="tagline-tab">It eats just like a chip</div>
    <div class="brand">KO.MU</div>

    <svg class="abs" style="left:0;top:0;" width="432" height="656" viewBox="0 0 432 656">
      <path d="M60 276 L60 588 L216 636 L372 588 L372 276" fill="none" stroke="var(--blue)" stroke-width="2"/>
    </svg>

    <div class="label-box">
      <div class="label-kicker">• QUALITY HANDMADE •</div>
      <div class="label-title">BEEF JERKY</div>
      <div class="label-origin">MADE IN HAWAII</div>
    </div>
    <div class="flavour-band">
      <div class="flavour-name">ORIGINAL</div>
      <div class="flavour-sub">(CHIPOTLE + TERIYAKI)</div>
    </div>
    <div class="claims">LOW FAT&nbsp; HIGH PROTEIN&nbsp; GLUTEN FREE</div>

    <p class="story">Made in the sunshine state with the finest cuts of Australian beef, handcrafted and seasoned in small batches.<br>We recommend sharing in the company of great friends over your favourite craft beer – but that's just us!</p>

    <p class="fine" style="left:89px;top:450px;width:262px;"><b>INGREDIENTS</b> :Beef, Soy Sauce (Water, Wheat Gluten, Salt, Sugar, Soybean, Caramel Coloring, Sodium benzoate, A preservative), MIRIN, BROWN SUGAR, CHIPOTLE CHILE, GROUND GINGER</p>
    <p class="fine" style="left:89px;top:490px;">Allergens Contains soy and wheat flour.</p>
    <p class="fine" style="left:89px;top:506px;width:150px;">Please store in a dry airtight container after opening and keep away from direct sunlight.</p>

    <div class="maker">
      <div class="brand-small">KO.MU</div>
      <p class="fine">221 Palm Lane, Honolulu, Hawai 96815<br>Phone : 808-555-0142<br>www.komusnacks.com</p>
    </div>

    <div class="nutrition">
      <h3>Nutrition Facts</h3>
      <div>Serving size 25g</div>
      <div>Serving per packet 3</div>
      <table>
        <tr class="head"><td></td><td>Per serving</td><td>Per 100g</td></tr>
        <tr><td><b>Energy</b></td><td>405kJ</td><td>1215kJ</td></tr>
        <tr><td><b>Protein</b></td><td>12.6g</td><td>38.0g</td></tr>
        <tr><td><b>Fat</b></td><td>2.2g</td><td>6.7g</td></tr>
        <tr><td><b>Carbohydrates</b></td><td>6.3g</td><td>18.9g</td></tr>
        <tr><td><b>Sugar</b></td><td>5.9g</td><td>17.8g</td></tr>
        <tr><td><b>Sodium</b></td><td>276mg</td><td>830mg</td></tr>
      </table>
      <div>All quantities above are averages.</div>
    </div>
  </section>

</main>
</body>
</html>
```